Vivaform - Fitness Coach. Needs a Business Card Design that I can also use for other advertising

Established 2012, I have finished the QPLB National Certificate in Fitness & Personal Training. Harrowgate First Aid Certificate. I have the Auckland 800m track records for MW45. I also came 1st at the 2012 Pacifica Games in 800 & 1500m. I am passionate about health & fitness and would like to help people reach their health & fitness goals. I also take health & fitness weekends. Main interests - Running, Weight Training, Yoga & Aqua Jogging. I like strength/power, but am femine.

Target Market(s)

Male or Female 18 and over that wants to improve their health & fitness

Industry/Entity Type

Advertising

Requirements
Must have
• my name: Lorissa K Dunmore contact details: lori@brightpath.co.nz mobile - 021 579318 URL name: facebook.com/lorissaKdunmore - VivaForm
Photo of Me

```html
<!DOCTYPE html>
<html lang="en">
<head>
<meta charset="utf-8">
<title>Lorissa K Dunmore – Business Card</title>
<link rel="stylesheet" href="https://fonts.googleapis.com/css2?family=Roboto+Condensed:wght@300;400;700&display=swap">
<style>
  :root {
    --page-bg: #ffffff;
    --ink: #000000;
    --leaf-dark: #1f3a12;
    --leaf-mid: #3f6f22;
    --leaf-light: #7fae3c;
    --panel: rgba(150, 150, 150, 0.55);
    --top-orange: #e8703a;
    --legging-grey: #3a3f44;
  }
  html, body {
    margin: 0;
    padding: 0;
    width: 1200px;
    height: 1000px;
    overflow: hidden;
    background: var(--page-bg);
  }
  .canvas {
    position: relative;
    width: 1200px;
    height: 1000px;
  }
  .card {
    position: absolute;
    left: 155px;
    top: 152px;
    width: 886px;
    height: 473px;
    overflow: hidden;
  }
  .card__hedge {
    position: absolute;
    inset: 0;
    display: block;
  }
  .card__portrait {
    position: absolute;
    left: 590px;
    top: 30px;
    width: 225px;
    height: 410px;
    display: block;
  }
  .card__panel {
    position: absolute;
    left: 0;
    top: 80px;
    width: 533px;
    height: 311px;
    background: var(--panel);
  }
  .card__text {
    position: absolute;
    right: 378px;
    top: 80px;
    width: 480px;
    text-align: right;
    font-family: "Roboto Condensed", "Arial Narrow", sans-serif;
    color: var(--ink);
  }
  .card__name {
    margin: 10px 0 0;
    font-size: 42px;
    font-weight: 700;
    line-height: 50px;
    letter-spacing: -0.5px;
  }
  .card__role {
    margin: 2px 0 0;
    font-size: 41px;
    font-weight: 300;
    line-height: 40px;
    letter-spacing: -0.5px;
  }
  .contact {
    list-style: none;
    margin: 7px 0 0;
    padding: 0;
  }
  .contact__item {
    display: flex;
    justify-content: flex-end;
    align-items: center;
    height: 50px;
    font-size: 23px;
    font-weight: 300;
  }
  .contact__icon {
    width: 34px;
    margin-left: 18px;
    display: flex;
    justify-content: center;
    align-items: center;
    font-weight: 700;
    font-size: 42px;
    line-height: 1;
  }
  .contact__square {
    width: 32px;
    height: 32px;
    background: var(--ink);
  }
</style>
</head>
<body>
<div class="canvas">
  <section class="card">
    <svg class="card__hedge" width="886" height="473" viewBox="0 0 886 473" role="img" aria-label="Leafy green hedge background">
      <defs>
        <linearGradient id="hedge" x1="0" y1="0" x2="0" y2="1">
          <stop offset="0" stop-color="var(--leaf-mid)"/>
          <stop offset="0.55" stop-color="var(--leaf-dark)"/>
          <stop offset="1" stop-color="var(--leaf-light)"/>
        </linearGradient>
      </defs>
      <rect width="886" height="473" fill="url(#hedge)"/>
    </svg>
    <svg class="card__portrait" width="225" height="410" viewBox="0 0 225 410" role="img" aria-label="Photo of the trainer jumping mid-air in an orange top and dark leggings">
      <defs>
        <linearGradient id="portrait" x1="0" y1="0" x2="0" y2="1">
          <stop offset="0" stop-color="var(--leaf-mid)" stop-opacity="0.6"/>
          <stop offset="0.3" stop-color="var(--top-orange)"/>
          <stop offset="0.55" stop-color="var(--top-orange)"/>
          <stop offset="0.7" stop-color="var(--legging-grey)"/>
          <stop offset="1" stop-color="var(--legging-grey)"/>
        </linearGradient>
      </defs>
      <rect width="225" height="410" rx="24" fill="url(#portrait)"/>
    </svg>
    <div class="card__panel"></div>
    <div class="card__text">
      <h1 class="card__name">Lorissa K Dunmore</h1>
      <p class="card__role">Fitness Instructor<br>and Personal Trainer</p>
      <ul class="contact">
        <li class="contact__item">lori@brightpath.co.nz<span class="contact__icon">@</span></li>
        <li class="contact__item">021 579318<span class="contact__icon">#</span></li>
        <li class="contact__item">Vivaform<span class="contact__icon"><span class="contact__square"></span></span></li>
      </ul>
    </div>
  </section>
</div>
</body>
</html>
```